Create a Graphic About YOURSELF and PixelHarbor

PixelHarbor would like you (designers) to create an awesome graphic to promote YOURSELF and your profile on PixelHarbor!

Your graphic should communicate your name, your services and should mention PixelHarbor.

The design should be perfect for sharing on Chatterly. Here's an example of what we'd like http://blog.pixelharbor-example.ca/article/333/pixelharbor-launches-3000-hire-me-social-design-contest

Once you submitted your design, we'd love you to share the design ('advertisement') and promote yourself and PixelHarbor to your friends and potential customers. So make your submissions great and get your friends to vote for your design by 'Liking' it on Chatterly!

Prizes:
$1500 - "PixelHarbor Community" prize awarded to the designer with the most Chatterly 'Likes'
5 x $50 for the next 5 'most liked' designs on Chatterly

$1000 - "Hire Me" prize awarded to the designer who receives the most client invites
5 x $50 for the next 5 'most invited' designers

In summary, this is a great opportunity for you to increase your exposure to PixelHarbor customers and win cash prizes. Show off your design skills and get hired by PixelHarbor customers from around the world!

Target Market(s)

Fans, friends and customers of YOU

Industry/Entity Type

Cash

Requirements
Must have
• 1) Include your PixelHarbor user name on the graphic so customers can find you in the PixelHarbor Designer Directory
2) Include the tagline "Hire Me on PixelHarbor.com!" in your graphic design.
3) Share your design's URL on our Chatterly wall at http://chatterly-example.com/pixelharbor and get your friends to 'like' your design.
Nice to have
• 1) Include a tagline that expresses your design approach/philosophy
2) Artwork dimensions: 403 x 403 px
3) You can submit more than 1 design!
Should not have
• You must own the copyright of any images you use including stock imagery.

```html
<!DOCTYPE html>
<html lang="en">
<head>
<meta charset="utf-8">
<title>lumastudio – Hire Me on PixelHarbor</title>
<link rel="stylesheet" href="https://fonts.googleapis.com/css2?family=Cabin:wght@400;500;700&display=swap">
<style>
  :root {
    --green-light: #8fd23f;
    --green-mid: #4fb83a;
    --green-deep: #1e9a3c;
    --ribbon: #f7941d;
    --ribbon-dark: #e57f12;
    --apple-glow: rgba(246, 214, 60, 0.28);
    --white: #ffffff;
    --yellow: #ffe600;
  }
  html, body {
    margin: 0;
    padding: 0;
    width: 1200px;
    height: 1200px;
    overflow: hidden;
    font-family: "Cabin", sans-serif;
  }
  .canvas {
    position: relative;
    width: 1200px;
    height: 1200px;
    overflow: hidden;
    background: radial-gradient(circle at 52% 52%, var(--green-light) 0%, var(--green-mid) 45%, var(--green-deep) 100%);
  }
  .corner-ribbon {
    position: absolute;
    left: 185px;
    top: 185px;
    width: 760px;
    height: 116px;
    margin-left: -380px;
    margin-top: -58px;
    transform: rotate(-45deg);
    background: linear-gradient(180deg, var(--ribbon) 0%, var(--ribbon-dark) 100%);
    border-top: 3px solid rgba(255,255,255,0.55);
    border-bottom: 3px solid rgba(255,255,255,0.55);
    box-sizing: border-box;
    display: flex;
    flex-direction: column;
    align-items: center;
    justify-content: center;
    color: var(--white);
    text-align: center;
  }
  .designer-name {
    font-size: 62px;
    font-weight: 700;
    line-height: 1;
    letter-spacing: 1px;
  }
  .designer-tagline {
    font-size: 21px;
    font-weight: 400;
    letter-spacing: 4px;
    margin-top: 4px;
  }
  .apple-artwork {
    position: absolute;
    left: 290px;
    top: 200px;
    width: 640px;
    height: 830px;
    border-radius: 48% 48% 50% 50% / 40% 40% 60% 60%;
    background: radial-gradient(ellipse at 50% 55%, var(--apple-glow) 0%, rgba(246,214,60,0.12) 55%, rgba(246,214,60,0) 75%);
  }
  .headline {
    position: absolute;
    left: 280px;
    width: 640px;
    top: 470px;
    margin: 0;
    text-align: center;
    color: var(--white);
    font-weight: 500;
  }
  .headline span { display: block; }
  .headline .line-top { font-size: 96px; line-height: 1.15; }
  .headline .line-large { font-size: 160px; line-height: 0.95; }
  .headline .line-bottom { font-size: 100px; line-height: 1.1; }
  .hire-line {
    position: absolute;
    left: 105px;
    top: 1085px;
    display: flex;
    align-items: center;
    gap: 20px;
    white-space: nowrap;
  }
  .hire-text {
    color: var(--yellow);
    font-size: 78px;
    font-weight: 400;
    letter-spacing: 4px;
    line-height: 1;
  }
  .platform-dot {
    width: 50px;
    height: 50px;
    border-radius: 50%;
    background: var(--white);
  }
  .platform-name {
    color: var(--white);
    font-size: 78px;
    font-weight: 700;
    letter-spacing: 2px;
    line-height: 1;
  }
</style>
</head>
<body>
  <main class="canvas">
    <div class="apple-artwork" role="img" aria-label="Outlined apple with two leaves drawn in an orange-to-yellow brush stroke"></div>

    <div class="corner-ribbon">
      <div class="designer-name">lumastudio</div>
      <div class="designer-tagline">clarity is my craft</div>
    </div>

    <h1 class="headline">
      <span class="line-top">Need</span>
      <span class="line-large">a fresh</span>
      <span class="line-bottom">logo?</span>
    </h1>

    <div class="hire-line">
      <span class="hire-text">Hire Me on</span>
      <span class="platform-dot"></span>
      <span class="platform-name">PixelHarbor</span>
    </div>
  </main>
</body>
</html>
```